BENEATH THE [HARBOR] OF A DAWN, Mend your road

We are looking for a cover refresh of an existing bestselling book that is going into 3rd edition print this year.
The book is an inspirational as well as educational book that has become recognized as one of the most comprehensive, actionable, personal and financial planning resources available today for families, individuals and business owners alike.
Comprised of three true stories of loss, learning to live and love again and a 30 page checklist at the back of the book it contains tips and strategies for everyone to help them to get their personal and financial lives in order while they can.
The cover must have the following:
1. Appeal to a broad audience/both personal and corporate
2. Include Mara Quellton Bestselling Author
3. Include introduction of a new Afterword
4. 3rd Edition
5. Colors to remain the same – red, black and white
6. The title must remain in caps and the word [HARBOR] must have the brackets around it
We have also added a current copy of the second edition to help you. For your information our website is www.thequelltonhouse.example
Reason: We have narrowed it down to our top 3 designs. We are submitting the covers to our community for them to pick the top cover. Good luck to everyone

```html
<!DOCTYPE html>
<html lang="en">
<head>
<meta charset="utf-8">
<title>Beneath the [Harbor] of a Dawn – Book Cover</title>
<link href="https://fonts.googleapis.com/css2?family=Bebas+Neue&family=Dancing+Script:wght@500;700&display=swap" rel="stylesheet">
<style>
  :root {
    --red: #e0141b;
    --black: #111111;
    --white: #ffffff;
    --page: #f2f2f2;
    --art-dark: #2a2a2a;
    --art-light: #e4e5e7;
  }
  * { margin: 0; padding: 0; box-sizing: border-box; }
  html, body {
    width: 1200px;
    height: 1000px;
    overflow: hidden;
    background: var(--page);
  }
  .canvas {
    position: relative;
    width: 1200px;
    height: 1000px;
    display: flex;
    align-items: center;
    justify-content: center;
  }
  .cover {
    position: relative;
    width: 620px;
    height: 900px;
    background: var(--white);
    border: 18px solid var(--red);
    overflow: hidden;
    box-shadow: 0 6px 24px rgba(0,0,0,0.12);
  }
  .title-line {
    position: absolute;
    left: 22px;
    font-family: "Bebas Neue", "Arial Narrow", sans-serif;
    color: var(--black);
    line-height: 1;
    white-space: nowrap;
  }
  .title-top {
    top: 30px;
    font-size: 112px;
    letter-spacing: 7px;
  }
  .title-band {
    position: absolute;
    left: 0;
    top: 150px;
    width: 520px;
    height: 158px;
    background: var(--red);
  }
  .title-keyword {
    position: absolute;
    left: 16px;
    top: 160px;
    font-family: "Bebas Neue", "Arial Narrow", sans-serif;
    font-size: 162px;
    line-height: 1;
    color: var(--white);
    letter-spacing: 3px;
    white-space: nowrap;
  }
  .title-bottom {
    top: 318px;
    font-size: 112px;
    letter-spacing: 18px;
  }
  .subtitle {
    position: absolute;
    left: 24px;
    top: 432px;
    font-family: "Dancing Script", cursive;
    font-weight: 500;
    font-size: 34px;
    color: var(--black);
  }
  .edition {
    position: absolute;
    left: 24px;
    top: 478px;
    font-family: "Bebas Neue", "Arial Narrow", sans-serif;
    font-size: 58px;
    line-height: 1;
    color: var(--black);
  }
  .edition sup {
    font-size: 28px;
    vertical-align: 22px;
    margin-right: 2px;
  }
  .cover-art {
    position: absolute;
    left: 300px;
    top: 530px;
    width: 266px;
    height: 170px;
    background: linear-gradient(225deg, var(--art-dark) 0%, #6b6e72 55%, var(--art-light) 100%);
  }
  .byline {
    position: absolute;
    right: 22px;
    top: 718px;
    font-family: "Dancing Script", cursive;
    font-weight: 700;
    font-size: 38px;
    color: var(--red);
  }
  .author {
    position: absolute;
    left: 24px;
    right: 18px;
    top: 778px;
    font-family: "Bebas Neue", "Arial Narrow", sans-serif;
    font-size: 66px;
    line-height: 1;
    letter-spacing: 13px;
    color: var(--black);
    white-space: nowrap;
    text-align: right;
  }
</style>
</head>
<body>
<main class="canvas">
  <section class="cover">
    <div class="title-line title-top">BENEATH THE</div>
    <div class="title-band"></div>
    <div class="title-keyword">[HARBOR]</div>
    <div class="title-line title-bottom">OF A DAWN</div>

    <p class="subtitle">Introduction of a new Afterword</p>
    <p class="edition">3<sup>RD</sup>EDITION</p>

    <div class="cover-art" role="img" aria-label="Photograph of a black fountain pen with a silver nib writing on the page"></div>

    <p class="byline">Bestselling Author</p>
    <p class="author">MARA QUELLTON</p>
  </section>
</main>
</body>
</html>
```